Flyer-Design für Pultrusionstechnologie
Zielgruppe
Wir sind eine europäische Vereinigung von Herstellern mit Pultrusionstechnologie. Unser Ziel ist, die Pultrusionstechnik bekannter zu machen, für Kunststoffhersteller und Kunden.
Aufgabenstellung
Der Text im Flyer ist von uns vorgegeben. Das Format des Flyers soll klassisch sein, A4, zweimal gefaltet.

```html
<!DOCTYPE html>
<html lang="en">
<head>
<meta charset="utf-8">
<title>PROFILA – Welcome to the World of Pultrusion</title>
<link rel="stylesheet" href="https://fonts.googleapis.com/css2?family=Barlow:wght@400;500;600&display=swap">
<style>
  :root {
    --frame: #000000;
    --paper: #ffffff;
    --blue: #0a62b3;
    --fold: #c9c9c9;
  }
  * { margin: 0; padding: 0; box-sizing: border-box; }
  html, body { width: 1200px; height: 864px; overflow: hidden; background: var(--frame); }
  .spread {
    position: relative; width: 1200px; height: 864px; background: var(--frame);
    font-family: "Barlow", Arial, sans-serif; color: var(--blue);
  }
  .sheet { position: absolute; left: 9px; top: 14px; width: 1182px; height: 836px; background: var(--paper); }
  .fold { position: absolute; top: 14px; width: 1px; height: 836px; background: var(--fold); }
  .abs { position: absolute; }
  .headline {
    position: absolute; font-weight: 500; font-size: 43px; line-height: 49px;
    letter-spacing: 1.5px; text-transform: uppercase; white-space: nowrap;
  }
  .copy { position: absolute; font-size: 12.6px; line-height: 16.2px; white-space: nowrap; }
  .photo { position: absolute; }
  .label { position: absolute; font-size: 8px; letter-spacing: .4px; white-space: nowrap; text-transform: uppercase; }
  .label-vert { transform: rotate(-90deg); transform-origin: left top; }
  .rule { position: absolute; background: var(--blue); }
  .sponsor { position: absolute; transform: translate(-50%, -50%); font-size: 10.5px; font-weight: 600; letter-spacing: .3px; white-space: nowrap; }
  .welcome { position: absolute; left: 1005px; top: 70px; font-size: 18px; line-height: 24px; letter-spacing: 1px; }
  .accent-square { position: absolute; left: 868px; top: 173px; width: 28px; height: 28px; background: var(--blue); }
  .brand { position: absolute; left: 854px; top: 700px; display: flex; align-items: center; gap: 10px; font-weight: 600; color: var(--blue); }
  .brand-square { width: 14px; height: 14px; background: var(--blue); }
  .brand-name { font-size: 34px; letter-spacing: 1px; line-height: 36px; }
  .brand-full { font-size: 10px; line-height: 13px; letter-spacing: 1px; text-transform: uppercase; margin-left: 4px; }
</style>
</head>
<body>
<main class="spread">
  <div class="sheet"></div>
  <div class="fold" style="left:403px"></div>
  <div class="fold" style="left:797px"></div>

  <!-- Applications panel -->
  <section class="panel-applications">
    <h2 class="headline" style="left:57px;top:68px">Typical<br>Applications</h2>
    <p class="copy" style="left:57px;top:187px">FRP profiles are predestined for use in a challenging<br>environment. The high-performance potential and outstanding<br>properties have made FRP profiles the material of choice<br>in many applications &amp; industries. Today you will find profiles<br>in building- und infrastructure sector, sports- and leisure,<br>mobility, wind-industry and many more.</p>

    <div class="photo" role="img" aria-label="Light blue stairway with handrail" style="left:57px;top:328px;width:275px;height:184px;background:linear-gradient(160deg,#eef0f2 0%,#e6e9ec 40%,#9fcbe8 55%,#8fc0e2 75%,#c9c5bd 100%)"></div>
    <div class="photo" role="img" aria-label="Grey building facade with window frame" style="left:222px;top:493px;width:157px;height:184px;background:linear-gradient(180deg,#a9d3f0 0%,#c9d4dc 18%,#e1e3e4 40%,#d0d3d5 100%)"></div>
    <div class="photo" role="img" aria-label="Blue street lamp mast against pale sky" style="left:83px;top:481px;width:121px;height:162px;background:linear-gradient(180deg,#d7e3ee 0%,#c8d8e6 100%)"></div>
    <div class="photo" role="img" aria-label="Steel space-frame scaffolding structure" style="left:57px;top:628px;width:242px;height:162px;background:linear-gradient(135deg,#1c2b36 0%,#2c3d49 50%,#3a4e5c 100%)"></div>

    <span class="rule" style="left:116px;top:314px;width:1px;height:34px"></span>
    <span class="label" style="left:123px;top:313px">Handrail/Stairway</span>
    <span class="label label-vert" style="left:361px;top:462px">Window Frame</span>
    <span class="rule" style="left:364px;top:469px;width:1px;height:34px"></span>
    <span class="label label-vert" style="left:56px;top:606px">Mast/ Pole</span>
    <span class="rule" style="left:57px;top:613px;width:35px;height:1px"></span>
    <span class="label" style="left:320px;top:761px">Scaffolding</span>
    <span class="rule" style="left:286px;top:774px;width:48px;height:1px"></span>
  </section>

  <!-- About panel -->
  <section class="panel-about">
    <h2 class="headline" style="left:427px;top:68px">About<br>PROFILA</h2>
    <p class="copy" style="left:427px;top:185px">PROFILA is the The Continental Profile Composites Alliance.<br>It was created in 1989 by the leading Pultruders in Europe.<br>With today 40 member companies/institutions PROFILA is the<br>largest pultrsuion network in Europe. The mission is to<br>support the growth of the composite profiles industry by maxi-<br>mizing external communication efforts and having an<br>actively contributing membership. PROFILA is open for membership<br>to all companies and organizations, wishing to participatei<br>promoting the responsible use of Fiber Reinforced Composite<br>Materials, and in the exchange of knowledge between<br>members.</p>

    <h2 class="headline" style="left:427px;top:600px">Sponsor<br>Members</h2>
    <span class="sponsor" style="left:461px;top:747px">ALTORA</span>
    <span class="sponsor" style="left:557px;top:747px">VERINOX</span>
    <span class="sponsor" style="left:652px;top:747px">FIBRANT</span>
    <span class="sponsor" style="left:748px;top:747px">Kelmora</span>
    <span class="sponsor" style="left:461px;top:783px">Holtzbrenner</span>
    <span class="sponsor" style="left:557px;top:783px">Kaiyo Glassworks</span>
    <span class="sponsor" style="left:652px;top:783px">Redmont</span>
    <span class="sponsor" style="left:748px;top:783px">Resinova</span>
  </section>

  <!-- Cover panel -->
  <section class="panel-cover">
    <p class="welcome">WELCOME TO<br>THE WORLD OF<br>PULTRUSION</p>
    <div class="photo" role="img" aria-label="Worker in a pultrusion plant handling white glass fibre rovings" style="left:853px;top:187px;width:338px;height:456px;background:linear-gradient(135deg,#eceeef 0%,#cfd3d6 35%,#b9bec2 55%,#dfe2e4 80%,#f2f3f4 100%)"></div>
    <div class="accent-square"></div>
    <div class="brand">
      <span class="brand-square"></span>
      <span class="brand-name">PROFILA</span>
      <span class="brand-full">Continental<br>Profile Composites<br>Alliance</span>
    </div>
  </section>
</main>
</body>
</html>
```